- Brightmoor Office Digest
- Links to the website
- I 'breathe fresh life' into office workplaces with these inspirational wellbeing newsletters! =)
- Other Facts

```html
<!DOCTYPE html>
<html lang="en">
<head>
<meta charset="utf-8">
<title>Brightmoor Office Digest – Well Being, Issue 05 2009</title>
<link rel="stylesheet" href="https://fonts.googleapis.com/css2?family=Arimo:wght@400;700&family=Dancing+Script:wght@600;700&family=Gochi+Hand&display=swap">
<style>
  :root {
    --brand-orange: #f26a10;
    --ink-navy: #1c2f6b;
    --ink-blue: #1d3f8f;
    --body-grey: #4a4f5a;
    --panel-blue: #c6def2;
    --panel-edge: #a9cbe8;
    --band-blue: #8fbfe6;
    --band-pale: #e8f3fb;
    --fact-blue: #5ea3d8;
    --paper: #ffffff;
    --melon-red: #e0343c;
    --melon-pink: #f08a8e;
    --leaf-green: #2f8a2c;
    --leaf-pale: #cfe7c4;
  }
  * { box-sizing: border-box; margin: 0; padding: 0; }
  html, body { width: 927px; height: 1200px; overflow: hidden; background: var(--paper); }
  .newsletter {
    position: relative; width: 927px; height: 1200px; overflow: hidden;
    background: var(--paper); font-family: "Arimo", Arial, sans-serif; color: var(--body-grey);
  }

  /* Masthead */
  .masthead-band {
    position: absolute; left: 430px; top: 0; width: 497px; height: 135px;
    background: linear-gradient(90deg, var(--paper) 0%, var(--band-pale) 25%, var(--band-blue) 100%);
  }
  .client-mark {
    position: absolute; left: 26px; top: 24px; display: flex; align-items: center; gap: 10px;
    font-family: "Arimo", Arial, sans-serif; font-weight: 700; font-size: 34px; color: var(--brand-orange);
  }
  .client-mark .dot { width: 22px; height: 22px; border-radius: 50%; background: var(--brand-orange); }
  .masthead-visual {
    position: absolute; left: 505px; top: 10px; width: 120px; height: 70px;
    background: linear-gradient(180deg, var(--melon-red) 0%, var(--melon-pink) 100%);
  }
  .masthead-title {
    position: absolute; left: 640px; top: 10px;
    font-family: "Dancing Script", cursive; font-weight: 700; font-size: 64px; color: var(--ink-navy); line-height: 1;
  }
  .issue-line {
    position: absolute; left: 664px; top: 106px; font-size: 15px; color: var(--ink-navy);
  }

  /* Left column */
  .hero-visual {
    position: absolute; left: 0; top: 150px; width: 250px; height: 505px;
    background: linear-gradient(180deg, #f3f0ec 0%, #e6dcd2 45%, #b9c9d8 100%);
  }
  .fact-box {
    position: absolute; left: 0; top: 660px; width: 246px; height: 235px;
    background: var(--fact-blue); color: var(--paper); padding: 12px 14px;
  }
  .fact-box h3 { font-family: "Gochi Hand", cursive; font-weight: 400; font-size: 28px; letter-spacing: 1px; margin-bottom: 6px; }
  .fact-box p { font-size: 13.2px; line-height: 1.35; }
  .leaf-visual {
    position: absolute; left: 0; top: 905px; width: 250px; height: 250px;
    background: linear-gradient(135deg, var(--leaf-pale) 0%, var(--leaf-green) 55%, var(--leaf-pale) 100%);
  }

  /* Intro */
  .intro {
    position: absolute; left: 372px; top: 138px; width: 525px;
    text-align: center; font-size: 17px; line-height: 1.35; color: var(--ink-blue);
  }
  .intro strong { font-weight: 700; }

  /* Trait panel */
  .traits {
    position: absolute; left: 246px; top: 286px; width: 660px; height: 614px;
    background: var(--panel-blue); border: 1px solid var(--panel-edge);
    padding: 12px 16px 10px 22px; text-align: justify; overflow: hidden;
  }
  .traits p { font-size: 12px; line-height: 1.42; color: var(--ink-blue); margin-bottom: 6px; }

  /* Swap this */
  .swap-title {
    position: absolute; left: 748px; top: 905px;
    font-family: "Dancing Script", cursive; font-weight: 700; font-size: 38px; color: var(--ink-navy);
  }
  .swap-copy {
    position: absolute; left: 470px; top: 952px; width: 430px;
    text-align: center; font-size: 15.5px; line-height: 1.32; color: var(--ink-blue);
  }
</style>
</head>
<body>
<main class="newsletter">
  <div class="masthead-band"></div>
  <div class="client-mark"><span class="dot"></span>Brightmoor</div>
  <div class="masthead-visual" role="img" aria-label="Photo of a watermelon slice"></div>
  <h1 class="masthead-title">Well Being</h1>
  <p class="issue-line">Issue 05 2009</p>

  <div class="hero-visual" role="img" aria-label="Photo of a slim woman in light clothing"></div>

  <aside class="fact-box">
    <h3>DID YOU KNOW?</h3>
    <p>The human body is comprised of 80% water and a mere 2% loss in body water can reduce your energy levels by 20 per cent! The effects of dehydration are poor concentration, tiredness and headaches, and you simply can't think as efficiently when you are dehydrated. So drink up!</p>
  </aside>

  <div class="leaf-visual" role="img" aria-label="Photo of green tea leaves"></div>

  <section class="intro">
    <p>Have you noticed some people seem to be able to eat what they like and still stay slim? Instead of secretly hating them, there are things we can learn about their habits and attitudes that allow them to stay lean. <strong>Here are the top 5 nutrition habits of naturally slim people:</strong></p>
  </section>

  <section class="traits">
    <p>1. They only eat when truly hungry. There are so many cues around us to eat when we are not even physically hungry – we grab a few lollies while we're at the desk, we have a biscuit from the kitchen with our morning tea, we eat a slice of cake because it's a colleague's birthday...the list is endless! Unfortunately, this non-hungry snacking really does add up. Naturally slim people eat when they are truly physically hungry, and not because they are bored, frustrated, celebrating, with a group of people, stressed or because 'it's time to eat'. They listen to their own body and hunger rather than watching the clock, eating because other people expect them to, or eating because it's there!</p>
    <p>2. Naturally slim and healthy people listen to their bodies. Some days we are hungrier than others, some days we crave different things. The body has its own innate wisdom, and some days our bodies require more fuel. Instead of dieting (trying to control or deny natural hunger), naturally slim people honour their hunger and nurture their bodies. Our bodies know exactly what is needed at any given moment, and when we tune in we're naturally led to the perfect foods for us.</p>
    <p>3. They enjoy a drink – and no, we are not talking about alcohol! Naturally slim people drink lots of water and stay well hydrated. They don't confuse thirst with hunger. Most times when we think we are hungry, we are really thirsty, and our first response to this feeling should be to have a glass of water.</p>
    <p>4. Healthy people don't do fad diets. Instead they eat in moderation, focus on nutrition and they don't really think about food unless they are physically hungry. Some days they eat more, some days they eat less, all depending on what their body needs. Dieting is denying yourself, and truly healthy people, inside and out, would never deny themselves. Instead they honour and nourish their bodies with the best quality food. Which leads to the final point:</p>
    <p>5. Naturally slim and healthy people get pleasure for example, when they eat a salad they think of all the vitamins, minerals and nutrients that they are providing their body and they feel good taking care of themselves. They don't see a salad as deprivation at all. Instead they feel nourished. Naturally slim people see food as fuel. They seek out the highest quality fuel, and gain pleasure from nourishing each cell with the best quality nutrients. When it comes down to it, no one is 'naturally' slim at all. We all have the choice of caring for, and nurturing, our bodies, or neglecting and creating health. It all lies in our approach and thoughts and behaviours – that's what creates our reality in all areas of life. Our body is always a reflection of what's going on inside, and when we have positive thoughts and a healthy attitude towards food, we're naturally guided to the best fuel to nourish ourselves and keep us at our perfect weight.</p>
  </section>

  <h2 class="swap-title">Swap this!</h2>
  <section class="swap-copy">
    <p>Coffee for green tea.<br>
    A skim latte has around 100-200 calories, and is a hit of false energy. Caffeine an enervate your body, and in the long term it leaves you fatigued. Herbal teas have only 5 calories, and each has their own natural benefits for your body. Green tea does have some caffeine (around 1/3 of the amount in coffee) but is also a powerful anti-oxidant, chamomile has calming properties, ginger root is excellent for improving circulation and peppermint tea aids digestion and is good for stress relief.</p>
  </section>
</main>
</body>
</html>
```